Maintenance Card

I am looking for a designed business tent card for the maintenance department of a hotel. The hotel is a Corvella Suites, I would like the logo to be on the card, and some verbiage telling the guest that while they were out maintenance came and repaired the issue(s) in the room. I would like the maintenance personelle to be able to check off the common complaints, HVAC, Plumbing, TV/Remote, Lights, other. There are some examples online, I would like it to be polished, and modern looking. My printer is www.printlark.com, and they only use certain file types. You can find their templates on their website. We would be printing a 4 x 3.5 tent business card. http://printlark.net/g/showStaticPage.do?page=download_templates-tent_card.html

Industry/Entity Type

Hotel

```html
<!DOCTYPE html>
<html lang="en">
<head>
<meta charset="utf-8">
<title>Maintenance Service Tent Card</title>
<link rel="stylesheet" href="https://fonts.googleapis.com/css2?family=Jost:wght@400;500&display=swap">
<style>
  :root {
    --red: #e30613;
    --red-dark: #b8000a;
    --red-text: #d0121b;
    --ink: #111111;
    --gray-top: #d2d2d2;
    --gray-bottom: #bdbdbd;
    --paper: #f7f7f7;
    --paper-shade: #e6e6e6;
    --dots: #444444;
  }
  html, body {
    margin: 0;
    padding: 0;
    overflow: hidden;
    background: #ffffff;
  }
  .card {
    position: relative;
    width: 1049px;
    height: 1200px;
    overflow: hidden;
    font-family: "Jost", "Futura", sans-serif;
    color: var(--ink);
    background: linear-gradient(180deg, #ffffff 0%, var(--paper) 40%, var(--paper-shade) 100%);
  }
  .header-band {
    position: absolute;
    left: 0; top: 0;
    width: 100%; height: 180px;
    background: linear-gradient(180deg, #dcdcdc 0%, var(--gray-top) 60%, #c6c6c6 100%);
  }
  .red-stripe {
    position: absolute;
    left: 0;
    width: 100%;
    height: 32px;
    background: linear-gradient(180deg, #ff2a2a 0%, var(--red) 45%, var(--red-dark) 100%);
    border-top: 2px solid #ffffff;
    border-bottom: 2px solid #ffffff;
    box-sizing: border-box;
  }
  .red-stripe.top { top: 179px; }
  .red-stripe.bottom { top: 1054px; }
  .footer-band {
    position: absolute;
    left: 0; top: 1086px;
    width: 100%; height: 114px;
    background: linear-gradient(180deg, #cfcfcf 0%, var(--gray-bottom) 100%);
  }
  .heading {
    position: absolute;
    left: 258px; top: 38px;
    margin: 0;
    font-weight: 400;
    font-size: 47px;
    line-height: 64px;
    color: var(--red);
  }
  .tool-tile {
    position: absolute;
    left: 52px;
    width: 133px; height: 134px;
    box-sizing: border-box;
    border: 2px solid var(--red);
    background: linear-gradient(135deg, #ffffff 0%, #e9eef0 100%);
    box-shadow: 2px 3px 5px rgba(0,0,0,0.25);
  }
  .tool-tile .art {
    position: absolute;
    inset: 14px;
    border-radius: 4px;
    background: linear-gradient(135deg, #d7dcdf 0%, #f2b500 55%, #6b6b6b 100%);
    opacity: 0.55;
  }
  .tool-tile.pliers { top: 68px; }
  .tool-tile.hammer { top: 235px; }
  .tool-tile.wrenches { top: 384px; }
  .option {
    position: absolute;
    display: flex;
    align-items: center;
    font-size: 37px;
    line-height: 1;
  }
  .checkbox {
    width: 20px; height: 20px;
    border: 3px solid var(--ink);
    box-shadow: 3px 3px 0 var(--ink);
    margin-right: 20px;
    background: #ffffff;
  }
  .option.hvac { left: 256px; top: 251px; }
  .option.tv { left: 645px; top: 251px; }
  .option.plumbing { left: 256px; top: 342px; }
  .option.lights { left: 645px; top: 342px; }
  .option.other { left: 256px; top: 437px; }
  .dots {
    position: absolute;
    height: 0;
    border-bottom: 3px dotted var(--dots);
  }
  .dots.other-1 { left: 423px; width: 537px; top: 467px; }
  .dots.other-2 { left: 426px; width: 537px; top: 538px; }
  .field {
    position: absolute;
    font-size: 37px;
    line-height: 1;
  }
  .field.serviced { left: 76px; top: 688px; }
  .field.date { left: 76px; top: 796px; }
  .field.time { left: 531px; top: 796px; }
  .dots.serviced-line { left: 316px; width: 654px; top: 718px; }
  .dots.date-line { left: 203px; width: 313px; top: 826px; }
  .dots.time-line { left: 658px; width: 314px; top: 826px; }
  .notice {
    position: absolute;
    left: 0; top: 936px;
    width: 100%;
    margin: 0;
    text-align: center;
    font-size: 37px;
    line-height: 49px;
    color: var(--red-text);
  }
  .tagline {
    position: absolute;
    left: 0; top: 1112px;
    width: 100%;
    margin: 0;
    text-align: center;
    font-size: 41px;
    line-height: 52px;
    color: var(--ink);
  }
</style>
</head>
<body>
<main class="card">
  <div class="header-band"></div>
  <div class="red-stripe top"></div>

  <h1 class="heading">We gladly performed the<br>following service request :</h1>

  <div class="tool-tile pliers"><div class="art" role="img" aria-label="Illustration of needle-nose pliers with yellow handles"></div></div>
  <div class="tool-tile hammer"><div class="art" role="img" aria-label="Illustration of a claw hammer with orange handle"></div></div>
  <div class="tool-tile wrenches"><div class="art" role="img" aria-label="Illustration of crossed wrench and adjustable pliers"></div></div>

  <div class="option hvac"><span class="checkbox"></span>HVAC</div>
  <div class="option tv"><span class="checkbox"></span>TV/Remote</div>
  <div class="option plumbing"><span class="checkbox"></span>Plumbing</div>
  <div class="option lights"><span class="checkbox"></span>Lights</div>
  <div class="option other"><span class="checkbox"></span>Other</div>
  <div class="dots other-1"></div>
  <div class="dots other-2"></div>

  <div class="field serviced">Serviced by :</div>
  <div class="dots serviced-line"></div>
  <div class="field date">Date :</div>
  <div class="dots date-line"></div>
  <div class="field time">Time :</div>
  <div class="dots time-line"></div>

  <p class="notice">If you have any questions or would like<br>additional service please call reception at '0'</p>

  <div class="red-stripe bottom"></div>
  <div class="footer-band"></div>
  <p class="tagline">"You do your thing. Leave the rest to us!"</p>
</main>
</body>
</html>
```